Maple Hollow Pet Services ABN 71 493 260 518 needs a Postcard Design

Genuine pet lover offering a professional and highly personalised pet service. I will visit your home daily to care for your pet in their own environment. THE OTHER OPTION FOR WHEN YOU GO ON HOLIDAYS. Dog Holiday Service (includes but not limited to) Feed, Water, Walk, Love & Play. Clean Litter Trays, Hutches & Cages. Administer Medication as Directed. Water Pot Plants & Collec Mail. Individual Dog Walking (Permanent or Casual). REASONABLE RATES. Police Check & References available upon request. Contact HARRIET 0412 684 219

```html
<!DOCTYPE html>
<html lang="en">
<head>
<meta charset="utf-8">
<title>Maple Hollow Pet Services – Postcard</title>
<link rel="stylesheet" href="https://fonts.googleapis.com/css2?family=Raleway:wght@500;600;700;800&display=swap">
<style>
  :root {
    --backdrop: #ececec;
    --card-orange: #ff8a10;
    --band-brown: #3a1c08;
    --ink-brown: #3b1d08;
    --text-orange: #ff9a24;
  }
  * { box-sizing: border-box; margin: 0; padding: 0; }
  html, body {
    width: 1200px;
    height: 771px;
    overflow: hidden;
    background: var(--backdrop);
    font-family: "Raleway", sans-serif;
  }
  .postcard {
    position: absolute;
    left: 110px;
    top: 75px;
    width: 980px;
    height: 621px;
    background: var(--card-orange);
    box-shadow: 0 6px 22px rgba(0,0,0,0.18);
    overflow: hidden;
  }
  .brand {
    position: absolute;
    top: 62px;
    left: 0;
    width: 100%;
    display: flex;
    justify-content: center;
    align-items: center;
    gap: 16px;
  }
  .brand-mark {
    width: 34px;
    height: 34px;
    background: var(--ink-brown);
  }
  .brand-name {
    font-weight: 700;
    font-size: 38px;
    letter-spacing: 2px;
    color: var(--ink-brown);
  }
  .service-band {
    position: absolute;
    top: 165px;
    left: 0;
    width: 100%;
    height: 290px;
    background: var(--band-brown);
    color: var(--text-orange);
    text-align: center;
    padding-top: 26px;
  }
  .service-title {
    font-weight: 800;
    font-size: 40px;
    letter-spacing: 1px;
    margin-bottom: 16px;
  }
  .service-list {
    list-style: none;
    font-weight: 600;
    font-size: 22px;
    line-height: 32px;
    letter-spacing: 0.3px;
  }
  .rates-row {
    margin-top: 24px;
    display: flex;
    justify-content: center;
    align-items: center;
    gap: 18px;
  }
  .rates {
    font-weight: 800;
    font-size: 40px;
    letter-spacing: 1px;
  }
  .rates-divider {
    width: 2px;
    height: 46px;
    background: var(--text-orange);
  }
  .credentials {
    text-align: left;
    font-weight: 600;
    font-size: 16px;
    line-height: 20px;
  }
  .contact-row {
    position: absolute;
    top: 490px;
    left: 0;
    width: 100%;
    display: flex;
    justify-content: center;
    align-items: center;
    gap: 22px;
    color: var(--ink-brown);
  }
  .phone-icon { width: 36px; height: 72px; }
  .contact-name {
    font-weight: 500;
    font-size: 56px;
    letter-spacing: 4px;
  }
  .contact-number {
    font-weight: 800;
    font-size: 56px;
    letter-spacing: 3px;
  }
</style>
</head>
<body>
  <main class="postcard">
    <header class="brand">
      <span class="brand-mark"></span>
      <span class="brand-name">Maple Hollow Pet Services</span>
    </header>

    <section class="service-band">
      <h1 class="service-title">DOG HOLIDAY SERVICE</h1>
      <ul class="service-list">
        <li>Feed, Water, Walk, Love &amp; Play. Clean Litter Trays, Hutches &amp; Cages</li>
        <li>Administer Medication as Directed. Water Pot Plants &amp; Collec Mail.</li>
        <li>Individual Dog Walking (Permanent or Casual)</li>
      </ul>
      <div class="rates-row">
        <span class="rates">REASONABLE RATES</span>
        <span class="rates-divider"></span>
        <span class="credentials">Police Check &amp; References<br>available upon request</span>
      </div>
    </section>

    <footer class="contact-row">
      <svg class="phone-icon" viewBox="0 0 36 72" aria-hidden="true">
        <path d="M30 4 H18 C10 4 6 12 6 36 C6 60 10 68 18 68 H30 V52 H22 C19 52 18 46 18 36 C18 26 19 20 22 20 H30 Z" fill="#3b1d08"/>
      </svg>
      <span class="contact-name">HARRIET</span>
      <span class="contact-number">0412 684 219</span>
      <svg class="phone-icon" viewBox="0 0 36 72" aria-hidden="true">
        <path d="M6 4 H18 C26 4 30 12 30 36 C30 60 26 68 18 68 H6 V52 H14 C17 52 18 46 18 36 C18 26 17 20 14 20 H6 Z" fill="#3b1d08"/>
      </svg>
    </footer>
  </main>
</body>
</html>
```